International Software Company Requires 3 Product Brochures.

Having just redesigned our website we require 3 brochures. 1 for each of our software products.
Our customers are global, blue chip, organisations and a professional, corporate style is required for each of the product brochures.
While each of the products are separate it should be clear that they are part of a family of products. All products are firmly marketed to the international oil and gas sector.
Rather than produce designs for 3 brochures straight away, we ask that designers produce a layout with a “unified theme” but with slight modifications adapted for each product. Please show the internal layout as well as the external cover.
Once we have chosen a design we will ask the designer to produce the three variations.
Designs should complement our new website design (not yet published) which can be found in the attachments section of this project.
The 3 products are…
QVT - time & cost estimation software
QVT is used by engineers to estimate the time and cost required to drill an oil or gas well. This involves modelling all the stages of drilling and then associating costs and risks to each stage before simulating the project using the Monte Carlo methodology to create a probabilistic result. The message is about delivering accurate and consistent results that communicate the project and risk to management. Attachment FJQVT1.jpg is a graphic we have previously used to illustrate the QVT process but we do not think is very effective.
LPW - materials & cost control software
LPW is used by drilling and logistics staff to keep very accurate and up-to-date track of all the costs and equipment associated with drilling a well. LPW quickly and accurately produces various cost and materials reports in what is a very complex and costly engineering project and where different departments (such as engineering or finance) have different needs. Attachment FJLPW1.jpg is a graphic we have previously used to illustrate the LPW process but we do not think is very effective.
ZHN – lessons learned software
ZHN is a web based system used by oil and gas companies to record and share lessons learned associated with drilling and maintaining wells. These are complex, expensive and often dangerous processes where it is vital that knowledge is shared between staff not matter where in the word they are located.
The brochure format we are looking for is double A4 bi-fold, (a front cover, 2 internal pages and a back page, A4 size.)
The brochures will be both printed and send out as PDFs to prospective clients.
Reason: We realise that our brief may not have been as clear as it could and a 3 brochure requirement may seem overwhelming.
We are updating the brief to ask designers to produce a layout with a “unified theme” but with slight modifications adapted for each product.
Initially we ask that designers give us an example of external and internal pages for a single product brochure as an example of the unified theme.
We are extending the deadline to allow for more entries.
We have just realised that the currency for this project was in USD and not GBP as we assumed. We have therefore substantially increased the
budget on this project, with a first place of $600-USD.
Engineers and financial staff within International oil and gas companies, i.e. GW, Pelta, Durango etc.
Oil And Gas

```html
<!DOCTYPE html>
<html lang="en">
<head>
<meta charset="utf-8">
<title>Corevane Systems – LPW Brochure</title>
<link rel="stylesheet" href="https://fonts.googleapis.com/css2?family=Oswald:wght@500;600&family=Open+Sans:wght@400;600;700&family=Tinos:wght@700&display=swap">
<style>
  :root{
    --teal:#2f6f7b;
    --teal-dark:#1f5561;
    --teal-light:#4a8a95;
    --ink:#222;
    --grey-bg:#ececec;
    --box-light:#f4f4f4;
    --box-dark:#b9b9b9;
    --white:#fff;
  }
  *{box-sizing:border-box;margin:0;padding:0}
  html,body{width:1200px;height:999px;overflow:hidden}
  body{background:var(--grey-bg);font-family:"Open Sans",Arial,sans-serif;color:var(--ink);position:relative}

  /* ---------- exterior spread ---------- */
  .exterior{position:absolute;left:40px;top:60px;width:650px;height:438px;display:flex;box-shadow:0 4px 14px rgba(0,0,0,.18)}
  .back-cover{width:325px;height:100%;background:linear-gradient(160deg,var(--teal-light),var(--teal-dark));position:relative;color:var(--white)}
  .contact{position:absolute;bottom:28px;font-size:6.5px;line-height:1.45}
  .contact h3{font-size:7px;font-weight:700;text-transform:uppercase;margin-bottom:1px}
  .contact-heading{position:absolute;left:24px;bottom:92px;font-size:9.5px;font-weight:700}
  .contact.europe{left:24px}
  .contact.america{left:180px}
  .front-cover{width:325px;height:100%;position:relative;background:var(--teal);overflow:hidden}
  .front-top{height:92px;background:var(--white);display:flex;align-items:center;justify-content:center;gap:8px}
  .brand-mark{width:14px;height:14px;border-radius:50%;background:var(--teal)}
  .brand-name{font-family:"Open Sans",Arial,sans-serif;font-weight:700;font-size:17px;color:var(--teal-dark);letter-spacing:.5px}
  .cover-image{position:absolute;top:92px;left:0;width:100%;height:210px;background:linear-gradient(135deg,#c9d6e0,#8fa6b8 55%,#5b7184)}
  .cover-swoosh{position:absolute;top:240px;left:0;width:100%;height:110px}
  .web{position:absolute;bottom:22px;left:0;width:100%;text-align:center;color:var(--white);font-size:9px;letter-spacing:3px}

  /* ---------- interior spread ---------- */
  .interior{position:absolute;left:522px;top:517px;width:650px;height:438px;background:var(--white);box-shadow:0 4px 14px rgba(0,0,0,.18);overflow:hidden}
  .page-divider{position:absolute;left:312px;top:0;width:1px;height:428px;background:#666}
  .bottom-band{position:absolute;left:0;bottom:0;width:100%;height:10px;background:linear-gradient(90deg,var(--teal-dark),var(--teal-light))}
  .intro{position:absolute;left:0;top:0;width:312px;height:107px;background:linear-gradient(180deg,var(--teal-light),var(--teal-dark));color:var(--white);padding:12px 10px 0 10px}
  .intro h1{font-family:"Oswald",sans-serif;font-weight:600;font-size:20px;letter-spacing:.3px;line-height:1.1;margin-bottom:9px}
  .intro p{font-size:6.2px;line-height:1.45;margin-bottom:8px}
  .reports{position:absolute;left:0;top:120px;width:312px}
  .report-group{margin-bottom:7px}
  .report-tab{display:block;width:fit-content;height:13px;line-height:13px;padding:0 14px 0 6px;background:var(--teal);color:var(--white);font-size:7.2px;font-weight:700;clip-path:polygon(0 0,92% 0,100% 100%,0 100%)}
  .report-group ul{list-style:none;margin-top:3px;padding-left:14px}
  .report-group li{font-size:6.6px;line-height:10px;position:relative;padding-left:13px}
  .report-group li::before{content:"•";position:absolute;left:0}

  .flow{position:absolute;left:312px;top:0;width:338px;height:428px}
  .node{position:absolute;background:linear-gradient(180deg,var(--box-light),var(--box-dark));border:1px solid #888;font-size:6.4px;text-align:center;display:flex;align-items:center;justify-content:center;text-transform:uppercase;line-height:1.35;padding:2px}
  .node.note{text-transform:none;text-align:left;justify-content:flex-start;font-size:6.8px;padding:4px 6px}
  .node.vertical{text-transform:none;font-size:6px;overflow:hidden}
  .node.vertical span{writing-mode:vertical-rl;text-align:center;line-height:1.3}
  .pointer{position:absolute;width:0;height:0;border-left:6px solid transparent;border-right:6px solid transparent}
  .pointer.down{border-top:7px solid var(--box-dark)}
  .pointer.up{border-bottom:7px solid var(--box-light)}
  .flow-caption{position:absolute;left:31px;top:380px;width:277px;text-align:center;font-family:"Tinos",serif;font-weight:700;font-size:12.5px;line-height:1.2}
</style>
</head>
<body>

<section class="exterior">
  <div class="back-cover">
    <div class="contact-heading">Address</div>
    <div class="contact europe">
      <h3>Europe</h3>
      12 Harbour Row<br>Aberdeen<br>AB11 4QT<br>Phone: +44 (0)1224 555 010<br>Email: europe@corevanesys.com
    </div>
    <div class="contact america">
      <h3>North America</h3>
      410 Meridian Park Dr<br>Suite 200<br>Houston, TX 77056<br>Phone: (713) 555 0148<br>Email: us@corevanesys.com
    </div>
  </div>
  <div class="front-cover">
    <div class="front-top">
      <span class="brand-mark"></span>
      <span class="brand-name">COREVANE SYSTEMS</span>
    </div>
    <div class="cover-image" role="img" aria-label="Photo of a businessman in a suit touching a floating digital interface with charts and a handshake"></div>
    <svg class="cover-swoosh" viewBox="0 0 325 110" preserveAspectRatio="none" aria-hidden="true">
      <defs>
        <linearGradient id="swooshGrey" x1="0" y1="0" x2="0" y2="1">
          <stop offset="0" stop-color="#8a8a8a"/><stop offset="1" stop-color="#3e3e3e"/>
        </linearGradient>
      </defs>
      <path d="M0 30 C80 0 170 10 230 25 C270 35 300 30 325 15 L325 110 L0 110 Z" fill="url(#swooshGrey)"/>
      <path d="M0 60 C90 30 180 40 240 55 C280 63 305 58 325 48 L325 110 L0 110 Z" fill="#2f6f7b"/>
    </svg>
    <div class="web">www.corevanesys.com</div>
  </div>
</section>

<section class="interior">
  <div class="intro">
    <h1>THE BUSINESS OF DRILLING WELLS</h1>
    <p>LPW provides detailed cost reporting, control and awareness across departments including PSCM, Drilling, Finance, Logistics and Inventory for a number of companies globally, including Northmoor, GW, Kestral and Ardent.</p>
    <p>LPW has a wide range of standard reports including...</p>
  </div>

  <div class="reports">
    <div class="report-group">
      <span class="report-tab">Tracking Reports:</span>
      <ul>
        <li>Purchases</li>
        <li>Stock/ Consignment Consumption</li>
        <li>All Rental Costs</li>
        <li>Rentals On-Hire</li>
        <li>All Personnel Costs</li>
        <li>Personnel On-Hire</li>
        <li>Tangible / Intangible Segregation</li>
      </ul>
    </div>
    <div class="report-group">
      <span class="report-tab">Display:</span>
      <ul>
        <li>All Costs</li>
        <li>Captured Only</li>
        <li>Non-Captured Only</li>
      </ul>
    </div>
    <div class="report-group">
      <span class="report-tab">Vendor Costs Report:</span>
      <ul>
        <li>By vendor/ alliance</li>
        <li>Restrict by cost code</li>
      </ul>
    </div>
    <div class="report-group">
      <span class="report-tab">Multi-Project Reporting:</span>
      <ul>
        <li>Detailed contract spend</li>
        <li>Vendor cost by code/ service</li>
      </ul>
    </div>
    <div class="report-group">
      <span class="report-tab">Vendor Project History:</span>
      <ul>
        <li>Group by cost type or code</li>
        <li>Report all projects</li>
      </ul>
    </div>
  </div>

  <div class="page-divider"></div>

  <div class="flow">
    <div class="node note" style="left:31px;top:20px;width:277px;height:48px">call off and track equipment and services. Accurate record of rentals and service costs is maintained in order to provide detailed daily cost breakdown.</div>
    <div class="pointer down" style="left:44px;top:68px"></div>

    <div class="node vertical" style="left:31px;top:80px;width:55px;height:68px"><span>@ &gt; 5% OF<br>Well<br>Procurement</span></div>
    <div class="pointer down" style="left:52px;top:148px"></div>
    <div class="node" style="left:97px;top:80px;width:114px;height:23px">Contract</div>
    <div class="pointer down" style="left:148px;top:103px"></div>
    <div class="node vertical" style="left:219px;top:80px;width:60px;height:68px"><span>@ &gt; 95% OF<br>Well<br>Procurement</span></div>
    <div class="pointer down" style="left:243px;top:148px"></div>
    <div class="node" style="left:97px;top:123px;width:114px;height:23px">Purchase Orders</div>

    <div class="node" style="left:31px;top:164px;width:112px;height:62px">Specific Purchase PO<br>with detailed cost</div>
    <div class="pointer down" style="left:40px;top:226px"></div>
    <div class="node" style="left:165px;top:164px;width:143px;height:62px">VSO per contract<br>services – high<br>dollar description<br>without details lines</div>

    <div class="node" style="left:31px;top:240px;width:80px;height:32px">Stock /<br>Inventory</div>
    <div class="node" style="left:114px;top:240px;width:80px;height:32px">Consignment</div>
    <div class="node" style="left:197px;top:240px;width:82px;height:32px">Rentals</div>
    <div class="node" style="left:31px;top:278px;width:80px;height:32px">Purchase<br>(Tangibles)</div>
    <div class="node" style="left:114px;top:278px;width:80px;height:32px">Personnel</div>
    <div class="node" style="left:197px;top:278px;width:82px;height:32px">Service</div>

    <div class="pointer up" style="left:180px;top:319px"></div>
    <div class="node note" style="left:31px;top:326px;width:277px;height:48px">LPW works to call off and track equipment and services. Accurate record of rentals and service costs is maintained in order to provide detailed daily cost breakdown.</div>

    <div class="flow-caption">Typical ERP<br>Drilling procurement Model<br>Supported by LPW</div>
  </div>

  <div class="bottom-band"></div>
</section>

</body>
</html>
```